Waterjet manufacturing company needs brochure design

We need a brochure that outlines why waterjet manufacturing is beneficial for a variety of industries, our capabilities, core competencies and competitive advantages (see attached documents). The design should include our logo and include the same colours. (Dark blue RGB – 2,86,162, Light Blue RGB – 0,146,201). The design should be very clean, professional and eye catching. I've attached a few photos that can be used. Regarding the photo of the robot, please make the background white.

Manufacturing, construction, aerospace, home building

• - exact Logo colours included in design (see description)
• - booklet style design (not tri-fold)
• - professional looking
• - Logo on front cover with writing underneath:
• High Quality
• Tight Tolerance
• Components
• - Plankrow, Ropelane, Vidstow and Pixelmorra icons in Contact Us section

```html
<!DOCTYPE html>
<html lang="en">
<head>
<meta charset="utf-8">
<title>Cascade Waterjet – Brochure Spread</title>
<link href="https://fonts.googleapis.com/css2?family=Carlito:wght@400;700&family=Tinos&family=Great+Vibes&display=swap" rel="stylesheet">
<style>
  :root{
    --brand-dark:#02569f;
    --deep:#1f4590;
    --navy:#2d5aa6;
    --band:#6a9ed3;
    --panel:#dbe6f3;
    --row-a:#c4daf1;
    --row-b:#dce8f5;
    --row-head:#8dbbe6;
    --ink:#111;
    --head-blue:#2b63b6;
    --white:#fff;
  }
  *{box-sizing:border-box;margin:0;padding:0}
  html,body{width:1200px;height:464px;overflow:hidden;background:var(--white)}
  .spread{position:relative;width:1200px;height:464px;overflow:hidden}

  /* Left page */
  .page-left{position:absolute;left:0;top:0;width:600px;height:464px;
    background:linear-gradient(160deg,#3b6cc0 0%,var(--navy) 45%,var(--deep) 100%)}
  .machine-photo{position:absolute;left:300px;top:0;width:300px;height:200px;
    background:radial-gradient(ellipse at 60% 35%,rgba(140,180,235,.45),rgba(45,90,166,0) 70%)}
  .page-shapes{position:absolute;left:0;top:0}
  .brand{position:absolute;left:35px;top:40px;display:flex;align-items:center;gap:7px}
  .brand-mark{width:14px;height:14px;background:var(--brand-dark)}
  .brand-name{font-family:"Carlito",sans-serif;font-weight:700;color:var(--brand-dark);
    font-size:19px;line-height:20px;letter-spacing:.5px}
  .parts-photo{position:absolute;left:33px;top:333px;width:158px;height:102px;
    background:radial-gradient(ellipse at 50% 60%,#6c6f75 0%,#2a2b2e 55%,#050505 100%)}

  .compare-title{position:absolute;left:222px;top:139px;font-family:"Carlito",sans-serif;
    font-size:13.5px;color:var(--white)}
  .compare-table{position:absolute;left:200px;top:161px;width:367px;border-collapse:collapse;
    font-family:"Carlito",sans-serif;font-size:8.7px;line-height:11.1px;color:var(--ink)}
  .compare-table th,.compare-table td{text-align:left;vertical-align:top;padding:0 3px 0 0}
  .compare-table th:first-child,.compare-table td:first-child{padding-left:7px}
  .compare-table thead tr{background:var(--row-head);height:17px}
  .compare-table thead th{padding-top:4px;font-weight:700}
  .compare-table .row-a{background:var(--row-a)}
  .compare-table .row-b{background:var(--row-b)}
  .compare-table td{padding-top:3px}
  .compare-table td.label{font-weight:700}
  .c-label{width:72px}.c-col{width:72px}

  /* Right page */
  .page-right{position:absolute;left:600px;top:0;width:600px;height:464px;background:var(--band)}
  .page-right .top-band{position:absolute;left:0;top:0;width:600px;height:54px;background:var(--navy)}
  .materials-title{position:absolute;left:100px;top:14px;color:var(--white);
    font-family:"Tinos",serif;font-size:15.5px;letter-spacing:.6px;white-space:nowrap}
  .materials-title .initial{font-family:"Great Vibes",cursive;font-size:40px;line-height:0;
    vertical-align:-6px;margin-right:-2px}
  .materials-box{position:absolute;left:29px;top:54px;width:541px;height:381px;background:var(--panel);
    padding:9px 23px 0 24px;font-family:"Tinos",serif;color:var(--ink)}
  .material{margin-bottom:6.2px}
  .material h3{font-weight:400;color:var(--head-blue);font-size:10.6px;line-height:11px}
  .material p{font-size:9.8px;line-height:10.2px;text-align:justify}
</style>
</head>
<body>
<div class="spread">
  <section class="page-left">
    <div class="machine-photo" role="img" aria-label="Waterjet cutting head close-up in blue tones"></div>
    <svg class="page-shapes" width="600" height="464" viewBox="0 0 600 464" aria-hidden="true">
      <defs>
        <linearGradient id="whiteFade" x1="0" y1="0" x2="0" y2="1">
          <stop offset="0.55" stop-color="#ffffff"/>
          <stop offset="1" stop-color="#b9cfea"/>
        </linearGradient>
      </defs>
      <path d="M0 0 H282 Q308 10 300 48 L0 360 Z" fill="var(--band)"/>
      <path d="M0 0 H228 Q262 14 246 50 L0 300 Z" fill="url(#whiteFade)"/>
    </svg>
    <div class="brand">
      <span class="brand-mark"></span>
      <span class="brand-name">CASCADE<br>WATERJET</span>
    </div>
    <div class="parts-photo" role="img" aria-label="Photo of waterjet-cut metal parts and a copper gear on a machine bed"></div>

    <h2 class="compare-title">Comparative Cutting Technologies</h2>
    <table class="compare-table">
      <colgroup><col class="c-label"><col class="c-col"><col class="c-col"><col class="c-col"><col class="c-col"></colgroup>
      <thead>
        <tr><th></th><th>WATERJET</th><th>PLASMA</th><th>LASER</th><th>EDM</th></tr>
      </thead>
      <tbody>
        <tr class="row-a" style="height:38px">
          <td class="label">PROCESS</td>
          <td>Erosion using high pressure water and garnet</td>
          <td>Burning/melting using a high temperature arc</td>
          <td>Melting using a concentrated laser light beam</td>
          <td>Erosion using an electrical discharge</td>
        </tr>
        <tr class="row-b" style="height:98px">
          <td class="label">SECONDARY PROCESSING</td>
          <td>Usually none. The cold cutting process typically leaves a finished edge product ready for end use</td>
          <td>Typically yes. Slag grinding required for removal of HAZ and flattening to eliminate distortion from heat.</td>
          <td>Sometimes yes. Required removal of oxidized edge and HAZ.</td>
          <td>Usually none. Very shallow HAZ imparted</td>
        </tr>
        <tr class="row-a" style="height:55px">
          <td class="label">MATERIALS CUT</td>
          <td>Virtually any material.</td>
          <td>Primarily steel, stainless steal and aluminum</td>
          <td>A variety of materials, but typically steel, stainless steel and aluminum</td>
          <td>Conductive materials</td>
        </tr>
        <tr class="row-b" style="height:22px">
          <td class="label">THICKNESS CUT</td>
          <td>Up to 2</td><td>Up to 2-3</td><td>Generally 1 or less</td><td>Generally 12 or less</td>
        </tr>
        <tr class="row-b" style="height:13px">
          <td class="label">ACCURACY</td>
          <td>Up to 0.001</td><td>Up to 0.010</td><td>Up to 0.001</td><td>Up to 0.001</td>
        </tr>
        <tr class="row-b" style="height:28px">
          <td class="label">MACHINE SETUP</td>
          <td>Same setup for all materials</td>
          <td>Different setup for different jobs</td>
          <td>Different gasses and parameters</td>
          <td>Different wire types for</td>
        </tr>
      </tbody>
    </table>
  </section>

  <section class="page-right">
    <div class="top-band"></div>
    <h2 class="materials-title"><span class="initial">M</span>aterials We Cut</h2>
    <div class="materials-box">
      <div class="material"><h3>METALS</h3>
        <p>•Abrasive Waterjet cutting is perfectly suited for all types of metal fabrication. Common metals like steel, copper and aluminum as well as brass, iron, titanium and tool steel can all be cut with ease, regardless of thickness.</p></div>
      <div class="material"><h3>COMPOSITES</h3>
        <p>•Composite materials are quickly becoming an integral part of our future. At the same time, the various layers of composites make them difficult to cut and shape using traditional methods. Fiberglass, carbon fiber, composite plastics, foams and even metals can all be precision cut using our waterjet technology without causing cracking, fraying or delamination.</p></div>
      <div class="material"><h3>STONE &amp; TILE</h3>
        <p>•Slate, marble, granite, engineered stone, ceramic, porcelain, limestone, soapstone and everything in between can be cut to spec fast and efficiently with minimal waste. Whether it’s for floors and counters, inlays and signage or intricate designs for artistic works and landscaping, Cascade Waterjet has your project covered. Compared to traditional cutting tools and CNC machines, our waterjet services can significantly help your business reduce work-in-process time, boost productivity and profits.</p></div>
      <div class="material"><h3>GLASS</h3>
        <p>•Piercing and cutting glass is simple and effective using waterjet technology leaving a perfect edge and eliminating any need to etch and break. Custom windows, doors, stained glass and even laminated ballistic glass can all be cut with precision.</p></div>
      <div class="material"><h3>PLASTIC, RUBBER &amp; ACRYLIC</h3>
        <p>•The material distortions that occur when machining plastic, rubber and acrylic on conventional CNC machines is nullified when using waterjet cutting. The cold-cutting process leaves a perfect edge without heating, warping or melting the material.</p></div>
      <div class="material"><h3>WOOD</h3>
        <p>•The wood materials used primarily in today’s industries are fabricated ones like plywood and veneer. Whether you’re cutting these composites, hardwood or softwood, waterjet cutting is a perfect option. Fast set up times, no splintering and minimal kerf allows for precise cutting without any thermal changes to the material.</p></div>
      <div class="material"><h3>CEMENT</h3>
        <p>•Abrasive waterjet cutting can be used effectively for the difficult task of breaking concrete down into smaller sections. No matter what you’re building, Cascade Waterjet can help shape your vision and bring your project to life.</p></div>
    </div>
  </section>
</div>
</body>
</html>
```